LINGERIE WEBSHOP - Velora casa

We are looking for design and layout design for our webshop. We are company that sells lingerie and other connected textile products liki payamas and etc..
Our website will have approx 500 different products within 2 main catogories Woman/Man) and approx. 10 subcategories
Here is what we expect form design:
-Color pallete should be black and white (if you wish you can add some accent color)
-we want to leave feeling to customers of good quality products towards to luxury
-UX should be simple. Feel free to suggest layout
-frontpage layout, product list layout, product description layout, blog layout
-responsive design, compatible with smartphone

Target Market(s)

woman buying for themself, man buying for woman

Industry/Entity Type

Lingerie

Logo Text

VELORA CASA

Number of Pages Required

4 page

Font styles to use
Sans Serif
Decorative

Requirements
Must have
• simple UX
Nice to have
• difference for sexy/luxury lingerie and daily/cozy lingerie
Should not have
• cheap feel, unreliable

```html
<!DOCTYPE html>
<html lang="en">
<head>
<meta charset="utf-8">
<title>Velora casa – Lingerie</title>
<link rel="stylesheet" href="https://fonts.googleapis.com/css2?family=Roboto:wght@400;500;700&family=Raleway:wght@400;500;700;800&display=swap">
<style>
:root{
  --green:#0a8a3b;
  --green-dark:#07722f;
  --ink:#222;
  --text:#444;
  --muted:#777;
  --nav:#2b2b2b;
  --footer:#2e2e2e;
  --grey-band:#ededed;
  --white:#fff;
  --line:#d9d9d9;
}
*{box-sizing:border-box;margin:0;padding:0}
html,body{width:1200px;height:4380px;overflow:hidden}
body{position:relative;font-family:"Roboto",Arial,sans-serif;color:var(--ink);background:var(--white)}
.abs{position:absolute}
/* top bar */
.topbar{left:0;top:0;width:1200px;height:61px;background:var(--green);color:var(--white);font-size:14px}
.topbar .links{position:absolute;left:113px;top:20px;display:flex;gap:22px}
.topbar .right{position:absolute;right:62px;top:19px;font-size:16px;letter-spacing:.3px}
/* header */
.header{left:0;top:61px;width:1200px;height:109px}
.social-top{position:absolute;left:118px;top:49px;display:flex;gap:22px}
.social-top span{width:10px;height:10px;background:#333;border-radius:50%;display:block}
.logo{position:absolute;left:480px;top:48px;width:236px;text-align:center;font-family:"Raleway",sans-serif;font-weight:400;font-size:29px;letter-spacing:1px;color:#333}
.search{position:absolute;left:738px;top:38px;width:233px;height:49px;border:1px solid var(--line);border-radius:25px;font-size:13px;color:var(--muted);padding:16px 0 0 19px}
.cart{position:absolute;left:1011px;top:52px;font-size:15px;color:var(--muted)}
/* nav */
.nav{left:0;top:170px;width:1200px;height:65px;background:var(--nav)}
.nav a{position:absolute;top:22px;color:var(--white);font-size:19px;text-decoration:none;letter-spacing:.3px}
/* hero */
.hero{left:0;top:235px;width:1200px;height:610px;
  background:
    radial-gradient(ellipse 300px 360px at 300px 330px,rgba(196,142,110,.55),rgba(196,142,110,0) 70%),
    radial-gradient(ellipse 180px 200px at 250px 360px,rgba(236,220,208,.7),rgba(236,220,208,0) 70%),
    linear-gradient(180deg,#7fc3cc 0%,#a7d6da 22%,#d5e5e1 40%,#efe4d4 58%,#e8d8c4 80%,#e3d1ba 100%)}
.hero-title{left:626px;top:412px;font-family:"Roboto",sans-serif;font-weight:700;font-size:58px;color:var(--green);letter-spacing:.5px}
.hero-text{left:631px;top:502px;width:420px;font-family:"Raleway",sans-serif;font-size:20px;line-height:34px;color:#444}
.btn{background:var(--green);color:var(--white);border-radius:30px;text-align:center;font-family:"Roboto",sans-serif}
.hero-btn{left:624px;top:624px;width:156px;height:49px;line-height:49px;font-size:19px}
.hero-dots span{display:block;width:9px;height:9px;border-radius:50%;background:var(--white);margin-bottom:10px}
h2.section{position:absolute;left:0;width:1200px;text-align:center;font-family:"Roboto",sans-serif;font-weight:700;font-size:40px;color:#222}
/* products */
.card{top:1066px;width:228px;height:308px;border:2px solid #dcdcdc;background:var(--white);box-shadow:0 2px 4px rgba(0,0,0,.12)}
.card .pic{position:absolute;left:30px;top:12px;width:164px;height:132px}
.card .name{position:absolute;top:166px;width:100%;text-align:center;font-weight:700;font-size:16px;color:#333}
.card .price{position:absolute;top:192px;width:100%;text-align:center;font-weight:700;font-size:13px;color:#333}
.card .stars{position:absolute;top:218px;left:0;width:100%;text-align:center}
.card .add{position:absolute;left:10px;top:268px;width:106px;height:28px;line-height:28px;font-size:11px}
.card .ic{position:absolute;top:267px;width:30px;height:30px;border-radius:50%;background:#ececec}
.dots{display:flex;gap:15px}
.dots span{width:11px;height:11px;border-radius:50%;background:#111;display:block}
.dots span.on{background:var(--green)}
/* about */
.about{left:0;top:1532px;width:1200px;height:561px;
  background:
    radial-gradient(ellipse 170px 280px at 980px 300px,rgba(186,201,222,.9),rgba(186,201,222,0) 75%),
    radial-gradient(ellipse 120px 140px at 960px 120px,rgba(170,120,95,.55),rgba(170,120,95,0) 75%),
    linear-gradient(90deg,#3f4f3a 0%,#6b7b5c 30%,#8e9a7d 55%,#7f8a6e 75%,#b9bfb2 92%,#e6e6e2 100%)}
.about-box{left:80px;top:1595px;width:714px;height:454px;background:rgba(60,60,60,.86);color:var(--white);padding:30px 46px}
.about-box h3{font-size:40px;font-weight:700;margin-bottom:22px}
.about-box p{font-family:Arial,sans-serif;font-size:13px;line-height:33.4px}
/* product detail */
.thumb{left:139px;width:91px;height:76px;border:2px solid #ccc;border-radius:4px;
  background:radial-gradient(ellipse 20px 32px at 50% 52%,#2a2a2a,rgba(42,42,42,0) 90%),linear-gradient(180deg,#f2f2f2,#e0e0e0)}
.main-pic{left:258px;top:2207px;width:381px;height:370px;border:2px solid #ccc;border-radius:5px;
  background:
    radial-gradient(ellipse 120px 190px at 50% 58%,rgba(25,25,25,.92),rgba(25,25,25,0) 80%),
    radial-gradient(ellipse 70px 70px at 50% 22%,rgba(150,105,80,.6),rgba(150,105,80,0) 80%),
    linear-gradient(180deg,#f4f4f4 0%,#e2e2e2 100%)}
.pd-title{left:673px;top:2244px;font-size:26px;font-weight:500;color:#222}
.pd-line{left:689px;font-size:21px;color:#333}
.pd-btn{left:689px;top:2487px;width:103px;height:28px;line-height:28px;font-size:12px}
/* testimonials */
.testi{left:0;top:2678px;width:1200px;height:556px;background:var(--grey-band)}
.avatar{left:566px;top:2847px;width:96px;height:96px;border-radius:50%;border:3px solid var(--green);
  background:radial-gradient(circle at 50% 40%,#d9c7b4,#8d8379 70%,#4a4540)}
.testi-text{left:205px;top:2980px;width:790px;text-align:center;font-size:14px;line-height:29px;color:#444}
.author{left:0;top:3100px;width:1200px;text-align:center;font-size:15px;color:#444}
/* blog */
.post{top:3431px;width:306px;height:366px;border:1px solid #e2e2e2;background:var(--white)}
.post .img{position:absolute;left:0;top:0;width:100%;height:183px}
.post .date{position:absolute;right:20px;top:8px;width:42px;height:140px;background:var(--white);border-radius:21px;overflow:hidden;text-align:center}
.post .date b{display:block;background:var(--green);color:var(--white);font-weight:400;font-size:20px;height:50px;line-height:50px}
.post .date i{display:block;font-style:normal;color:#2196d3;font-size:11px;line-height:14px;margin-top:6px}
.post .by{position:absolute;top:212px;width:100%;text-align:center;font-weight:700;font-size:16px;color:#333}
.post .by svg{vertical-align:-6px;margin-right:6px}
.post .txt{position:absolute;top:252px;left:22px;width:262px;text-align:center;font-size:14.5px;line-height:26px;color:#555}
.post .more{position:absolute;left:85px;top:353px;width:136px;height:38px;line-height:38px;font-size:15px}
/* footer */
.footer{left:0;top:3961px;width:1200px;height:419px;background:var(--footer);color:var(--white)}
.f-logo{left:151px;top:4020px;font-family:"Raleway",sans-serif;font-size:29px;letter-spacing:1px}
.f-about{left:147px;top:4077px;width:352px;font-size:16px;line-height:34px}
.f-soc{left:130px;top:4190px;display:flex;gap:16px}
.f-soc span{display:block;width:36px;height:36px;border:1.5px solid var(--white);border-radius:50%}
.f-head{font-size:19px;font-weight:500;letter-spacing:.3px}
.f-contact{left:616px;font-size:14px;line-height:28px}
.f-links{left:867px;font-size:16px}
.cards{left:811px;top:4258px;display:flex;gap:8px}
.cards span{display:block;width:40px;height:26px;border-radius:3px;background:#5a5a5a}
.copy{left:124px;top:4303px;font-size:13px}
</style>
</head>
<body>

<!-- top bar -->
<div class="abs topbar">
  <div class="links">
    <span><svg width="10" height="13" viewBox="0 0 10 13"><path d="M5 0a5 5 0 0 1 5 5c0 3.5-5 8-5 8S0 8.5 0 5a5 5 0 0 1 5-5z" fill="#fff"/><circle cx="5" cy="5" r="2" fill="#0a8a3b"/></svg> Store Location</span>
    <span>▮ Track Order</span>
    <span>● Login/Register</span>
  </div>
  <div class="right">✆ HOTLINE &nbsp;|&nbsp; ENGLISH ▾ &nbsp;|&nbsp; USD ▾</div>
</div>

<!-- header -->
<div class="abs header">
  <div class="social-top"><span></span><span></span><span></span><span></span><span></span></div>
  <div class="logo">VELORA CASA</div>
  <div class="search">Search Here
    <svg class="abs" style="right:14px;top:14px" width="18" height="18" viewBox="0 0 18 18"><circle cx="7.5" cy="7.5" r="5.5" fill="none" stroke="#0a8a3b" stroke-width="2.4"/><path d="M11.5 11.5l5 5" stroke="#0a8a3b" stroke-width="2.6"/></svg>
  </div>
  <div class="cart"><svg width="22" height="18" viewBox="0 0 22 18" style="vertical-align:-3px"><path d="M0 1h4l3 11h11l3-8H6" fill="none" stroke="#0a8a3b" stroke-width="2.4"/><circle cx="8" cy="16" r="2" fill="#0a8a3b"/><circle cx="17" cy="16" r="2" fill="#0a8a3b"/></svg> Cart</div>
</div>

<!-- nav -->
<nav class="abs nav">
  <a style="left:206px">FRONT PAGE</a>
  <a style="left:383px">WOMEN</a>
  <a style="left:510px">MEN</a>
  <a style="left:605px">CHILDREN</a>
  <a style="left:762px">ABOUT US</a>
  <a style="left:913px">CONTACT</a>
</nav>

<!-- hero -->
<div class="abs hero" role="img" aria-label="Photo of a model in a floral bikini seated on a sunny beach"></div>
<svg class="abs" style="left:0;top:760px" width="1200" height="90" viewBox="0 0 1200 90">
  <path d="M0 22 C250 95 600 90 1200 10 L1200 90 L0 90Z" fill="#fff"/>
  <path d="M0 22 C250 95 600 90 1200 10 L1200 18 C600 88 250 98 0 30Z" fill="#0a8a3b"/>
</svg>
<div class="abs hero-title">VELORA CASA</div>
<div class="abs hero-text">Sed ut perspiciatis unde omnis iste natus sitvoluptatem accusantiumdoloremque laudantium</div>
<div class="abs btn hero-btn">BUY NOW</div>
<div class="abs hero-dots" style="left:1079px;top:421px"><span></span><span></span><span style="background:#0a8a3b"></span></div>

<!-- featured -->
<h2 class="section" style="top:952px">FEATURED PRODUCTS</h2>

<div class="abs card" style="left:109px">
  <div class="pic" role="img" aria-label="Black lace suspender belt" style="background:radial-gradient(ellipse 62px 58px at 50% 45%,#1b1b1b 40%,rgba(27,27,27,0) 100%)"></div>
  <div class="name">PRODUCT NAME</div><div class="price">$38.15</div>
  <div class="stars"><svg width="86" height="14" viewBox="0 0 86 14"><g fill="#f0a500"><path id="st" d="M7 0l2 4.6 5 .5-3.8 3.3 1.1 5L7 10.8 2.7 13.4l1.1-5L0 5.1l5-.5z"/><use href="#st" x="18"/><use href="#st" x="36"/><use href="#st" x="54"/><use href="#st" x="72"/></g></svg></div>
  <div class="btn add">ADD TO CART</div>
  <div class="ic" style="left:150px"></div><div class="ic" style="left:187px"></div>
</div>
<div class="abs card" style="left:357px">
  <div class="pic" role="img" aria-label="Nude lace bralette" style="background:radial-gradient(ellipse 62px 58px at 50% 45%,#efcdbd 40%,rgba(239,205,189,0) 100%)"></div>
  <div class="name">PRODUCT NAME</div><div class="price">$38.15</div>
  <div class="stars"><svg width="86" height="14" viewBox="0 0 86 14"><g fill="#f0a500"><use href="#st"/><use href="#st" x="18"/><use href="#st" x="36"/><use href="#st" x="54"/><use href="#st" x="72"/></g></svg></div>
  <div class="btn add">ADD TO CART</div>
  <div class="ic" style="left:150px"></div><div class="ic" style="left:187px"></div>
</div>
<div class="abs card" style="left:605px">
  <div class="pic" role="img" aria-label="Black crew-neck T-shirt" style="background:radial-gradient(ellipse 62px 58px at 50% 45%,#111 45%,rgba(17,17,17,0) 100%)"></div>
  <div class="name">PRODUCT NAME</div><div class="price">$38.15</div>
  <div class="stars"><svg width="86" height="14" viewBox="0 0 86 14"><g fill="#f0a500"><use href="#st"/><use href="#st" x="18"/><use href="#st" x="36"/><use href="#st" x="54"/><use href="#st" x="72"/></g></svg></div>
  <div class="btn add">ADD TO CART</div>
  <div class="ic" style="left:150px"></div><div class="ic" style="left:187px"></div>
</div>
<div class="abs card" style="left:853px">
  <div class="pic" role="img" aria-label="Patterned men's boxer briefs" style="background:radial-gradient(ellipse 62px 56px at 50% 45%,#2f2f2f 45%,rgba(47,47,47,0) 100%)"></div>
  <div class="name">PRODUCT NAME</div><div class="price">$38.15</div>
  <div class="stars"><svg width="86" height="14" viewBox="0 0 86 14"><g fill="#f0a500"><use href="#st"/><use href="#st" x="18"/><use href="#st" x="36"/><use href="#st" x="54"/><use href="#st" x="72"/></g></svg></div>
  <div class="btn add">ADD TO CART</div>
  <div class="ic" style="left:150px"></div><div class="ic" style="left:187px"></div>
</div>
<div class="abs dots" style="left:566px;top:1453px"><span></span><span></span><span></span></div>

<!-- about -->
<div class="abs about" role="img" aria-label="Photo of a model in pale blue lingerie on a garden terrace"></div>
<div class="abs about-box">
  <h3>ABOUT US</h3>
  <p>At the location of the busiest shopping center in Marenvik - Arvena center, the Velora casa boutique has been operating for 20 years. The store offers a large selection of favorite high-quality fashion lingerie brands for women, men and childrenNew in the offer! New collection of Italian Velmara socks. Well-known Italian brand available in Croatia only in Velora casa fashion stores. Various models , solid weaving, modern colors and patterns are just some of the qualities offered by Velmara .Sophisticated lingerie , modern patterns and colors, made of high quality materia with selected details are named Oriel, Lunessa, Clara Vesti, Dornel, Mira Castelli, Soleva, Nivra, Terro, Alvina, Brisa, Odel, Marveo, Corvina, Sweet Lune Girl, Peralta , Nodo, Ravel, Tessa, Velmara.</p>
</div>

<!-- product detail -->
<div class="abs thumb" style="top:2218px" role="img" aria-label="Kaftan thumbnail"></div>
<div class="abs thumb" style="top:2309px" role="img" aria-label="Kaftan thumbnail"></div>
<div class="abs thumb" style="top:2402px" role="img" aria-label="Kaftan thumbnail"></div>
<div class="abs thumb" style="top:2497px" role="img" aria-label="Kaftan thumbnail"></div>
<div class="abs main-pic" role="img" aria-label="Model wearing a sheer black beach kaftan over a black bikini"></div>
<div class="abs pd-title">Norel beach kaftan in black</div>
<div class="abs pd-line" style="top:2301px;left:680px;font-weight:700;font-size:23px">£12.00</div>
<div class="abs pd-line" style="top:2347px">Free delivery (Ts&amp;Cs apply)</div>
<div class="abs pd-line" style="top:2390px">COLOUR: Solid black</div>
<div class="abs pd-line" style="top:2436px">SIZE: XL</div>
<div class="abs btn pd-btn">ADD TO CART</div>

<!-- testimonials -->
<div class="abs testi"></div>
<h2 class="section" style="top:2744px">TESTMONIALS</h2>
<svg class="abs" style="left:153px;top:2865px" width="120" height="94" viewBox="0 0 120 94"><g fill="#cfcfcf"><path d="M0 94V50C0 22 14 4 44 0v16C30 20 24 30 24 44h26v50z"/><path d="M66 94V50C66 22 80 4 110 0v16C96 20 90 30 90 44h26v50z"/></g></svg>
<svg class="abs" style="left:932px;top:3075px" width="116" height="98" viewBox="0 0 120 94"><g fill="#cfcfcf" transform="rotate(180 60 47)"><path d="M0 94V50C0 22 14 4 44 0v16C30 20 24 30 24 44h26v50z"/><path d="M66 94V50C66 22 80 4 110 0v16C96 20 90 30 90 44h26v50z"/></g></svg>
<div class="abs avatar" role="img" aria-label="Portrait of the reviewer"></div>
<div class="abs testi-text">Sed ut perspiciatis unde omnis iste natus error sit voluptatem accusantium doloremque laudantium, totam rem aperiam, eaque ipsa quae ab illo inventore veritatis et quasi architecto beatae vitae dicta sunt explicabo. Nemo enim ipsam voluptatem quia voluptas.</div>
<div class="abs author">By Author Name</div>
<div class="abs dots" style="left:566px;top:3161px;gap:11px"><span></span><span></span><span class="on"></span></div>

<!-- blog -->
<h2 class="section" style="top:3328px;font-size:34px;font-weight:500">LATEST &nbsp;BLOG</h2>

<div class="abs post" style="left:116px">
  <div class="img" role="img" aria-label="Red sale banner with a model" style="background:radial-gradient(ellipse 60px 40px at 40% 10%,#3a2a28,rgba(58,42,40,0) 90%),linear-gradient(90deg,#d9161c,#e8333a)"></div>
  <div class="date"><b>11</b><i>F<br>E<br>B</i></div>
  <div class="by"><svg width="26" height="26" viewBox="0 0 26 26"><circle cx="13" cy="13" r="13" fill="#222"/><circle cx="13" cy="10" r="4.5" fill="#fff"/><path d="M5 21a8 8 0 0 1 16 0z" fill="#fff"/></svg>BY ADMIN</div>
  <div class="txt">Dear customers, take advantage of a 15% discount on our webshop and in our store in the Arvena Center</div>
  <div class="btn more">READ MORE</div>
</div>
<div class="abs post" style="left:452px">
  <div class="img" role="img" aria-label="Green sale banner with a model" style="background:radial-gradient(ellipse 60px 40px at 40% 10%,#3a3230,rgba(58,50,48,0) 90%),linear-gradient(90deg,#8cb94a,#a6cc6a)"></div>
  <div class="date"><b>11</b><i>F<br>E<br>B</i></div>
  <div class="by"><svg width="26" height="26" viewBox="0 0 26 26"><circle cx="13" cy="13" r="13" fill="#222"/><circle cx="13" cy="10" r="4.5" fill="#fff"/><path d="M5 21a8 8 0 0 1 16 0z" fill="#fff"/></svg>BY ADMIN</div>
  <div class="txt">Dear customers, stop by our store in the Arvena Center and save 20-30% on certain items when</div>
  <div class="btn more">READ MORE</div>
</div>
<div class="abs post" style="left:789px">
  <div class="img" role="img" aria-label="Wire heart with rose petals on pink" style="background:radial-gradient(ellipse 70px 55px at 45% 50%,rgba(160,50,55,.55),rgba(160,50,55,0) 90%),linear-gradient(135deg,#e2c3c5,#d3a8ab)"></div>
  <div class="date"><b>11</b><i>F<br>E<br>B</i></div>
  <div class="by"><svg width="26" height="26" viewBox="0 0 26 26"><circle cx="13" cy="13" r="13" fill="#222"/><circle cx="13" cy="10" r="4.5" fill="#fff"/><path d="M5 21a8 8 0 0 1 16 0z" fill="#fff"/></svg>BY ADMIN</div>
  <div class="txt">Dear customers, tae advantage of a 15% discount on our webshop and in our store in the Arvena center</div>
  <div class="btn more">READ MORE</div>
</div>
<div class="abs dots" style="left:583px;top:3885px;gap:6px"><span class="on" style="width:9px;height:9px"></span><span style="width:9px;height:9px"></span><span style="width:9px;height:9px"></span></div>

<!-- footer -->
<footer class="abs footer"></footer>
<div class="abs f-logo" style="color:#fff">VELORA CASA</div>
<div class="abs f-about" style="color:#fff">Neque porro quisquam est qui dolorem ipsum quia dolor sit amet, consectetur, adipisci velit. "There is no one who loves pain itself,</div>
<div class="abs f-soc"><span></span><span></span><span></span><span></span><span></span></div>

<div class="abs f-head" style="left:566px;top:4015px;color:#fff">CONTACT US</div>
<svg class="abs" style="left:572px;top:4068px" width="14" height="20" viewBox="0 0 14 20"><path d="M7 0a7 7 0 0 1 7 7c0 5-7 13-7 13S0 12 0 7a7 7 0 0 1 7-7z" fill="#fff"/><circle cx="7" cy="7" r="2.6" fill="#2e2e2e"/></svg>
<div class="abs f-contact" style="top:4063px;color:#fff">2190 Linden Row,<br>Harbor Vale, CA</div>
<svg class="abs" style="left:571px;top:4135px" width="18" height="18" viewBox="0 0 18 18"><path d="M4 1l3 4-2 2c1 2.5 3.5 5 6 6l2-2 4 3-2 3C8 17 1 10 1 3z" fill="#fff"/></svg>
<div class="abs f-contact" style="top:4129px;color:#fff">Tel: &nbsp;(555) 014-2290</div>
<svg class="abs" style="left:570px;top:4181px" width="20" height="14" viewBox="0 0 20 14"><rect x="0" y="0" width="20" height="14" fill="#fff"/><path d="M0 0l10 8 10-8" fill="none" stroke="#2e2e2e" stroke-width="1.6"/></svg>
<div class="abs f-contact" style="top:4173px;color:#fff">Email:info@veloracasa.com</div>

<div class="abs f-head" style="left:862px;top:4007px;color:#fff">QUICK LINK</div>
<div class="abs f-links" style="top:4065px;color:#fff;line-height:34.5px">
  <div>» &nbsp;FRONT PAGE</div><div>» &nbsp;WOMEN</div><div>» &nbsp;MEN</div><div>» &nbsp;CHILDREN</div><div>» &nbsp;ABOUT US</div>
</div>
<div class="abs cards"><span></span><span></span><span></span><span></span><span></span><span></span></div>
<div class="abs copy" style="color:#fff">Copyrights © 2020 Copyrights Company Name | All Rights Reserved</div>

</body>
</html>
```